update and create new Tessho Kan Judo Website

We require a new and modernised website for our Karate school.
Website currently is www.Tesshokan.com
Please check the current state of the website to start off with.
The basis of the brief attached is to provide context on what we want for the new website.

1) Please read through the build brief attached.
2) We are looking for a vendor who can service our organisation's website needs in future and ongoing.
3) Our budget is more than currently able to post on here and is subject to discussion should we choose you as our vendor. The amount initially is priced to be between $700.00 - $1000.00 AUD for the selected website.
4) easy and simple use and communication is a must.
5) this build request is subject to updating should we require further needs on the website.
6) The reason we have chosen the "refundable" option at this stage is because we've never used Pixel Hive before. However the winning vendor will receive full commission and continued pay ongoing for future management of the website.

Thank you
Milo
Updates

Hi Designers and Vendors Regarding this website. Our budget is set at approx. $1000.00 with ongoing work commission to run the website. I advise you read what is re

Industry/Entity Type

Communication

```html
<!DOCTYPE html>
<html lang="en">
<head>
<meta charset="utf-8">
<title>Tessho Kan Judo — Dojo</title>
<link rel="stylesheet" href="https://fonts.googleapis.com/css2?family=Oswald:wght@400;500;600;700&family=Open+Sans:wght@300;400&family=Noto+Sans+JP:wght@400&display=swap">
<style>
  :root {
    --header-bg: #262626;
    --page-bg: #000000;
    --footer-bg: #2b2b2b;
    --text-white: #ffffff;
    --text-soft: #c4c4c4;
    --nav-text: #b9cfe0;
    --nav-line: #d9d9d9;
    --accent: #a9d3ef;
    --frame-gold: #a49462;
    --frame-mauve: #6f5a74;
    --frame-red: #8e1b24;
    --frame-green: #33452d;
    --fill-navy: #37316c;
    --motif-white: #f4f2fb;
    --fill-cream: #ece2c6;
    --motif-plum: #6b3645;
    --fill-mist: #dcd5d8;
    --motif-yellow: #d8cc10;
    --fill-pink: #fd79c7;
    --fill-red: #cf1f2a;
    --fill-coral: #f2906a;
    --fill-brown: #4e2c2c;
    --motif-gold: #d9ac6a;
    --fill-sage: #97a06a;
  }
  * { box-sizing: border-box; margin: 0; padding: 0; }
  html, body { width: 1200px; height: 1000px; overflow: hidden; background: var(--page-bg); }
  body { position: relative; font-family: "Open Sans", Arial, sans-serif; color: var(--text-white); }

  .site-header {
    height: 132px;
    background: linear-gradient(180deg, #2e2e2e, var(--header-bg));
    text-align: center;
    padding-top: 3px;
  }
  .site-title {
    font-family: "Oswald", Arial, sans-serif;
    font-weight: 600;
    font-size: 44px;
    line-height: 54px;
    letter-spacing: -1px;
    text-transform: uppercase;
  }
  .site-tagline {
    width: 960px;
    margin: 6px auto 0;
    font-weight: 300;
    font-size: 20px;
    line-height: 26px;
    color: var(--text-soft);
  }

  .main-nav {
    display: flex;
    height: 51px;
    border-top: 1px solid var(--nav-line);
    border-bottom: 1px solid var(--nav-line);
    background: var(--page-bg);
  }
  .main-nav a {
    flex: 0 0 200px;
    display: flex;
    align-items: center;
    justify-content: center;
    border-left: 1px solid var(--nav-line);
    font-family: "Oswald", Arial, sans-serif;
    font-weight: 500;
    font-size: 15px;
    letter-spacing: -0.3px;
    text-transform: uppercase;
    color: var(--nav-text);
    text-decoration: none;
  }
  .main-nav a:first-child { border-left: none; }
  .main-nav a.is-current { color: var(--text-white); }

  .card-grid { position: absolute; left: 120px; top: 237px; width: 980px; }
  .card-row { display: flex; }
  .card-row + .card-row { position: absolute; top: 354px; left: 0; }
  .card { width: 244px; padding-right: 14px; display: flex; flex-direction: column; align-items: flex-start; }

  .card-media { width: 198px; height: 132px; border: 5px solid; }
  .frame-gold { border-color: var(--frame-gold); }
  .frame-mauve { border-color: var(--frame-mauve); }
  .frame-red { border-color: var(--frame-red); }
  .frame-green { border-color: var(--frame-green); }

  .tile-navy { background: radial-gradient(circle at 50% 50%, var(--motif-white) 0, #b9b5d6 22%, var(--fill-navy) 48%); }
  .tile-cream { background: radial-gradient(circle at 50% 50%, var(--motif-plum) 0, #8a5a62 26%, var(--fill-cream) 50%); }
  .tile-mist { background: radial-gradient(circle at 50% 50%, var(--motif-yellow) 0, #dcd270 26%, var(--fill-mist) 50%); }
  .tile-pink { background: radial-gradient(circle at 50% 50%, #ffffff 0, #ffd2ec 24%, var(--fill-pink) 50%); }
  .tile-red { background: linear-gradient(135deg, var(--fill-red), #e8787c 50%, var(--fill-red)); }
  .tile-coral { background: linear-gradient(90deg, #fbe3d6, var(--fill-coral) 50%, #fbe3d6); }
  .tile-brown { background: radial-gradient(circle at 50% 50%, #8a6143 0, var(--fill-brown) 70%); }
  .tile-sage { background: linear-gradient(135deg, #c9cdb0, var(--fill-sage) 50%, #c9cdb0); }

  .card-title {
    margin-top: 13px;
    font-family: "Oswald", Arial, sans-serif;
    font-weight: 500;
    font-size: 21px;
    line-height: 26px;
    letter-spacing: -1px;
  }
  .card-title.jp { font-family: "Noto Sans JP", sans-serif; font-weight: 400; font-size: 19px; letter-spacing: 0; }
  .card-text {
    margin-top: 7px;
    font-size: 11.5px;
    line-height: 17px;
    width: 224px;
  }
  .card-text.jp { font-family: "Noto Sans JP", sans-serif; font-size: 11px; }
  .address-list { list-style: none; margin-top: 7px; font-size: 11.5px; line-height: 17px; }
  .address-list li + li { margin-top: 17px; }

  .more-button {
    margin-top: 29px;
    width: 109px;
    height: 33px;
    border: 2px solid var(--accent);
    display: flex;
    align-items: center;
    justify-content: center;
    font-family: "Oswald", Arial, sans-serif;
    font-weight: 500;
    font-size: 12px;
    color: var(--accent);
    text-decoration: none;
  }
  .more-button.loose { margin-top: 32px; }

  .site-footer { position: absolute; left: 0; bottom: 0; width: 1200px; height: 10px; background: var(--footer-bg); }
</style>
</head>
<body>
  <header class="site-header">
    <h1 class="site-title">Tessho Kan Judo</h1>
    <p class="site-tagline">Welcome to Tessho Kan Judo, to our Dojo and to our events as we invite all Judo-ka and visitors world-wide to experience what we do and invite them to part-take in our Judo activities.</p>
  </header>

  <nav class="main-nav">
    <a href="#">Home</a>
    <a href="#">About</a>
    <a href="#">News</a>
    <a href="#" class="is-current">Dojo</a>
    <a href="#">Get Started</a>
    <a href="#">Contact</a>
  </nav>

  <main class="card-grid">
    <div class="card-row">
      <article class="card">
        <div class="card-media frame-gold tile-navy" role="img" aria-label="White flower crest on navy"></div>
        <h2 class="card-title">Dojo Kun</h2>
        <p class="card-text">In mollis erat mattisy nequelisis sit amet ultricieser erarutrum. Cras facilisis, nulla vel viverra</p>
        <a class="more-button" href="#">more</a>
      </article>
      <article class="card">
        <div class="card-media frame-mauve tile-cream" role="img" aria-label="Plum flower crest on cream"></div>
        <h2 class="card-title">Hombu Dojo</h2>
        <p class="card-text">In mollis erat mattisy nequelisis sit amet ultricieser erarutrum. Cras facilisis, nulla vel viverra</p>
        <a class="more-button" href="#">more</a>
      </article>
      <article class="card">
        <div class="card-media frame-red tile-mist" role="img" aria-label="Yellow flower crest on pale grey"></div>
        <h2 class="card-title">International Dojo<br>Alliance</h2>
        <p class="card-text">In mollis erat mattisy nequelisis sit amet ultricieser erarutrum. Cras facilisis, nulla vel viverra</p>
        <a class="more-button" href="#">more</a>
      </article>
      <article class="card">
        <div class="card-media frame-green tile-pink" role="img" aria-label="White blossom crest on pink"></div>
        <h2 class="card-title">Dojo Locations</h2>
        <ul class="address-list">
          <li>12 Harbour Lane WESTFIELD VIC 3500</li>
          <li>8 Cedar Road MILLBROOK VIC 3280</li>
          <li>27 Ridge Avenue PINE HOLLOW QLD 4060</li>
        </ul>
        <a class="more-button loose" href="#">more</a>
      </article>
    </div>

    <div class="card-row">
      <article class="card">
        <div class="card-media frame-green tile-red" role="img" aria-label="Red and white key fret pattern"></div>
        <h2 class="card-title jp">尊重</h2>
        <p class="card-text jp">道場では互いを敬い、礼に始まり礼に終わる心を大切にします。先輩と後輩が共に学び、日々の稽古を通じて誠実な人間関係を築きます。相手を思いやる気持ちが強さの源であり、感謝の心を忘れません。</p>
        <a class="more-button" href="#">more</a>
      </article>
      <article class="card">
        <div class="card-media frame-red tile-coral" role="img" aria-label="Coral and white arrow feather pattern"></div>
        <h2 class="card-title jp">精神</h2>
        <p class="card-text jp">心と体を鍛える稽古を重ね、困難に向き合う不屈の精神を養います。静かな集中と強い意志が技を磨き、道場の外でも生きる力となります。毎日の努力が自信を育てます。</p>
        <a class="more-button" href="#">more</a>
      </article>
      <article class="card">
        <div class="card-media frame-mauve tile-brown" role="img" aria-label="Gold hemp leaf pattern on brown"></div>
        <h2 class="card-title jp">紀律</h2>
        <p class="card-text jp">時間を守り、道具を整え、決まりを尊重することが上達への近道です。日々の小さな積み重ねが確かな力となり、心を整えます。</p>
        <a class="more-button" href="#">more</a>
      </article>
      <article class="card">
        <div class="card-media frame-gold tile-sage" role="img" aria-label="White scroll pattern on sage green"></div>
        <h2 class="card-title">Affiliations</h2>
        <p class="card-text">In mollis erat mattisy nequelisis sit amet ultricieser erarutrum. Cras facilisis, nulla vel viverra</p>
        <a class="more-button" href="#">more</a>
      </article>
    </div>
  </main>

  <footer class="site-footer"></footer>
</body>
</html>
```